Business Van Wrap- Must be UNIQUE!

Business Wrap for a 2023 Halvorn Cargex 480QX Twinwell. High Roof , Extended length. No Windows on side door or rear. The van is black from factory. We would like to utilize the factory black color as to save on the wrap project. We are looking for a Unique, innovative, creative, and effective design. Not looking for a cookie cutter, copy and paste design.
We are distributors of tire repair materials, hand tools, power tools, tire changer machinery, chemicals, wheel accessories,

Must have our company Logo, colors, Company Name: Corbet Parts Industries- A Division of Vennmark Industries. Address: 418 Quenwick Lane, Unit 7, Islandia, NY 11562 Phone: 833-555-0172

products we sell are the following: Tire repair Tools, Cleaner, Vulcanizing Cement, Bead Sealer, Patches, Plugs and Strings, Clip-On Wheel Weights, Adhesive wheel weights, Valve Stems, Valve cores, Valve Caps, TPMS Sensors, TPMS Replacement valves, Large Bore Valves, Tire Changers, Wheel Balancers, Mount/Demount Heads, Air Compressors, Hydraulic Jacks, Pneumatic Hoses, Head Inserts, Air Chucks, Inflators, Gauges, Impact Wrenches, Impact Sockets, Tire Mounting Paste, Tire Lube, Dovrin Crayomarks, Safety Equipment, OEM Lug Nuts, Lug Bolts, Wheel Spacers.

Target Market(s)

tire repair shops, mechanic shops, tire franchises, used tire businesses

Industry/Entity Type

tire industry

Requirements
Must have
• must have our logo, our address, contact number and website address
Nice to have
• would like graphics that represent our business, our company colors..black, red, white, grey
Should not have
• not too much going on

```html
<!DOCTYPE html>
<html lang="en">
<head>
<meta charset="utf-8">
<title>Corbet Parts Industries – Van Wrap Layout</title>
<link href="https://fonts.googleapis.com/css2?family=Saira:wght@500;600&family=Barlow+Condensed:ital,wght@1,600&family=Barlow:ital,wght@1,500&display=swap" rel="stylesheet">
<style>
  :root {
    --wrap-black: #111112;
    --panel-edge: #2a2a2c;
    --brand-red: #d32f34;
    --brand-white: #f2f2f2;
    --brand-grey: #b9b9bc;
    --tread-grey: #5a5a5e;
    --page: #ffffff;
  }
  html, body {
    margin: 0;
    width: 1200px;
    height: 1200px;
    overflow: hidden;
    background: var(--page);
  }
  .canvas { position: relative; width: 1200px; height: 1200px; }

  .wrap-panel {
    position: absolute;
    background: var(--wrap-black);
    border: 2px solid var(--panel-edge);
    border-radius: 18px;
    overflow: hidden;
  }
  .side-panel  { left: 60px;  top: 80px;  width: 1080px; height: 380px; }
  .front-panel { left: 60px;  top: 560px; width: 500px;  height: 560px; }
  .rear-panel  { left: 620px; top: 560px; width: 520px;  height: 560px; }

  .tread-graphic {
    position: absolute;
    z-index: 0;
    background: linear-gradient(160deg, rgba(90,90,94,0) 0%, rgba(90,90,94,.85) 45%, rgba(70,70,74,.6) 100%);
  }
  .side-panel .tread-graphic { right: 0; top: 0; width: 260px; height: 100%; }
  .rear-panel .tread-graphic { right: 0; top: 180px; width: 170px; height: 380px; }

  .brand-lockup { position: absolute; z-index: 1; display: flex; flex-direction: column; align-items: flex-start; }
  .brand-row { display: flex; align-items: center; }
  .brand-square { border: 6px solid var(--brand-red); box-sizing: border-box; flex: none; }
  .brand-name {
    font-family: "Saira", sans-serif;
    font-weight: 600;
    color: var(--brand-white);
    text-transform: uppercase;
    line-height: 1;
    white-space: nowrap;
  }
  .brand-tagline {
    font-family: "Saira", sans-serif;
    font-weight: 500;
    color: var(--brand-grey);
    text-transform: uppercase;
    white-space: nowrap;
  }

  .side-panel .brand-lockup { left: 300px; top: 70px; }
  .side-panel .brand-square { width: 84px; height: 84px; margin-right: 22px; }
  .side-panel .brand-name { font-size: 46px; }
  .side-panel .brand-tagline { font-size: 17px; letter-spacing: 6px; margin-top: 16px; }

  .red-band {
    position: absolute;
    z-index: 1;
    background: var(--brand-red);
    color: var(--brand-white);
    font-family: "Barlow Condensed", sans-serif;
    font-style: italic;
    font-weight: 600;
    display: flex;
    align-items: center;
    justify-content: center;
    white-space: nowrap;
  }
  .side-panel .red-band { left: 270px; top: 235px; width: 730px; height: 52px; font-size: 36px; transform: rotate(-1deg); }

  .address {
    position: absolute;
    z-index: 1;
    margin: 0;
    font-family: "Barlow", sans-serif;
    font-style: italic;
    font-weight: 500;
    color: var(--brand-white);
    line-height: 1.35;
  }
  .side-panel .address { left: 40px; top: 240px; font-size: 13px; }

  .social-dots { position: absolute; z-index: 1; display: flex; gap: 8px; }
  .social-dot { width: 16px; height: 16px; border-radius: 50%; background: var(--brand-red); }
  .side-panel .social-dots { left: 40px; top: 205px; }

  .front-panel .brand-lockup { left: 50%; top: 250px; transform: translateX(-50%); align-items: center; }
  .front-panel .brand-square { width: 30px; height: 30px; border-width: 3px; margin-right: 10px; }
  .front-panel .brand-name { font-size: 19px; }
  .front-panel .brand-tagline { font-size: 7px; letter-spacing: 2.5px; margin-top: 6px; }

  .rear-panel .red-band.phone-band { left: 30px; top: 60px; width: 460px; height: 60px; font-size: 42px; }
  .rear-panel .brand-lockup { left: 40px; top: 235px; }
  .rear-panel .brand-square { width: 56px; height: 56px; margin-right: 14px; border-width: 5px; }
  .rear-panel .brand-name { font-size: 26px; }
  .rear-panel .brand-tagline { font-size: 11px; letter-spacing: 4px; margin-top: 12px; }
  .rear-panel .social-dots { left: 40px; top: 388px; }
  .rear-panel .red-band.web-band { left: 0; top: 420px; width: 330px; height: 44px; font-size: 28px; justify-content: flex-start; padding-left: 40px; box-sizing: border-box; }
  .rear-panel .address { left: 40px; top: 488px; font-size: 12px; }
</style>
</head>
<body>
<main class="canvas">

  <section class="wrap-panel side-panel" aria-label="Side wrap layout">
    <div class="tread-graphic" role="img" aria-label="Grey distressed tire tread marks sweeping across the rear of the van"></div>
    <div class="social-dots"><span class="social-dot"></span><span class="social-dot"></span><span class="social-dot"></span></div>
    <p class="address">418 Quenwick Lane,<br>Unit 7, Islandia, NY 11562</p>
    <div class="brand-lockup">
      <div class="brand-row">
        <span class="brand-square"></span>
        <span class="brand-name">Corbet Parts Industries</span>
      </div>
      <span class="brand-tagline">Specializing in tire solutions</span>
    </div>
    <div class="red-band">833-555-0172 | corbetpartsind.com</div>
  </section>

  <section class="wrap-panel front-panel" aria-label="Front hood wrap layout">
    <div class="brand-lockup">
      <div class="brand-row">
        <span class="brand-square"></span>
        <span class="brand-name">Corbet Parts Industries</span>
      </div>
      <span class="brand-tagline">Specializing in tire solutions</span>
    </div>
  </section>

  <section class="wrap-panel rear-panel" aria-label="Rear doors wrap layout">
    <div class="tread-graphic" role="img" aria-label="Grey distressed tire tread mark running up the rear doors"></div>
    <div class="red-band phone-band">833-555-0172</div>
    <div class="brand-lockup">
      <div class="brand-row">
        <span class="brand-square"></span>
        <span class="brand-name">Corbet Parts Industries</span>
      </div>
      <span class="brand-tagline">Specializing in tire solutions</span>
    </div>
    <div class="social-dots"><span class="social-dot"></span><span class="social-dot"></span><span class="social-dot"></span></div>
    <div class="red-band web-band">corbetpartsind.com</div>
    <p class="address">418 Quenwick Lane,<br>Unit 7, Islandia, NY 11562</p>
  </section>

</main>
</body>
</html>
```